Electrical Contracting business card design

We need a simple business card design for an Electrical Contracting business. A simple design would be appreciated
This company has 2 directors so on one it would have Colin Marsh & another with Dana Marsh.
Updates

Reason: Hello A few designers have asked for a logo unfortunately we don't have one so have extended deadline to see who can help us out with this. CHEERS

Reason: Waiting for business partner to return from xmas break. cheers

Industry/Entity Type

Business

Contact Information for Business Card

Volmera Electrical Services P/L
REC: 36074
Residential Commercial Industrial
Service-Repairs-Renovations-Installations-Telephone-Data
Colin Marsh-Ph: 0433 517 862
Email: colin@volmeraelectrical.com.au

Requirements
Should not have
• The design should not have any electrical appliances in it ie: power-points, leads, houses etc.

```html
<!DOCTYPE html>
<html lang="en">
<head>
<meta charset="utf-8">
<title>Volmera Electrical Services – Business Card</title>
<link rel="stylesheet" href="https://fonts.googleapis.com/css2?family=Bebas+Neue&family=Ubuntu:wght@500&display=swap">
<style>
  :root {
    --backdrop: #3b4747;
    --card-white: #ffffff;
    --ink: #333333;
    --brand-blue: #1b4a84;
    --tile-deep: #2d2f9e;
    --tile-bright: #2f78d6;
    --tile-violet: #5a3cb8;
    --mark-white: #f2f2f2;
  }
  * { box-sizing: border-box; margin: 0; padding: 0; }
  html, body {
    width: 1200px; height: 1000px; overflow: hidden;
    background: var(--backdrop);
  }
  .card {
    position: absolute;
    width: 640px; height: 366px;
    left: 280px;
    overflow: hidden;
  }
  .card--front { top: 70px; background: var(--card-white); }
  .card--back { top: 560px; background: var(--brand-blue); }

  .tile {
    position: absolute;
    background: linear-gradient(135deg, var(--tile-bright) 0%, var(--tile-deep) 55%, var(--tile-violet) 100%);
  }
  .tile-row--top .tile { top: 0; height: 52px; width: 116px; }
  .tile-row--main .tile { top: 118px; height: 92px; width: 126px; }

  .brand {
    position: absolute;
    display: flex; align-items: center; gap: 12px;
    font-family: "Bebas Neue", sans-serif;
    letter-spacing: 0.5px;
  }
  .brand__dot { border-radius: 50%; flex: none; }
  .card--front .brand { left: 24px; top: 60px; color: var(--ink); font-size: 31px; }
  .card--front .brand__dot { width: 38px; height: 38px; background: var(--brand-blue); }
  .card--back .brand { left: 70px; top: 150px; color: var(--mark-white); font-size: 46px; }
  .card--back .brand__dot { width: 56px; height: 56px; background: var(--mark-white); }

  .person {
    position: absolute; right: 30px; top: 80px;
    text-align: right;
    font-family: "Bebas Neue", sans-serif;
    color: var(--ink);
  }
  .person__name { font-size: 26px; line-height: 1; }
  .person__role { font-size: 15px; line-height: 1; }

  .details {
    position: absolute; left: 0; right: 0; top: 228px;
    text-align: center;
    font-family: "Ubuntu", sans-serif; font-weight: 500;
    font-size: 13.5px; line-height: 1.45;
    color: var(--ink);
  }
</style>
</head>
<body>
  <section class="card card--front">
    <div class="tile-row--top">
      <div class="tile" role="img" aria-label="Close-up photo of a circuit board in blue tones" style="left:130px"></div>
      <div class="tile" role="img" aria-label="Close-up photo of a circuit board in blue tones" style="left:252px"></div>
      <div class="tile" role="img" aria-label="Close-up photo of a circuit board in blue tones" style="left:374px"></div>
      <div class="tile" role="img" aria-label="Close-up photo of a circuit board in blue tones" style="left:496px"></div>
    </div>

    <div class="brand">
      <span class="brand__dot"></span>
      <span class="brand__name">Volmera Electrical Services</span>
    </div>

    <div class="person">
      <div class="person__name">Colin Marsh</div>
      <div class="person__role">Director</div>
    </div>

    <div class="tile-row--main">
      <div class="tile" role="img" aria-label="Close-up photo of circuit board components in blue and violet" style="left:60px"></div>
      <div class="tile" role="img" aria-label="Close-up photo of circuit board components in blue and violet" style="left:192px"></div>
      <div class="tile" role="img" aria-label="Close-up photo of circuit board components in blue and violet" style="left:324px"></div>
      <div class="tile" role="img" aria-label="Close-up photo of circuit board components in blue and violet" style="left:456px"></div>
    </div>

    <div class="details">
      <p>Volmera Electrical Services P/L REC :</p>
      <p>36074 Residential Commercial Industrial Service</p>
      <p>- Repairs - Renovations - Installations</p>
      <p>Ph: 0433 517 862&nbsp;&nbsp; Email: colin@volmeraelectrical.com.au</p>
    </div>
  </section>

  <section class="card card--back">
    <div class="brand">
      <span class="brand__dot"></span>
      <span class="brand__name">Volmera Electrical Services</span>
    </div>
  </section>
</body>
</html>
```